Ad Design for a child care centre

Bright Pebbles Child Care Centre offers a safe, nurturing environment where your child will get the attention and care that he or she needs. Our ratio of children to adults is always within state guidelines - and often even higher - to make certain each child receives top-quality care
We are also state licensed as a Child Care facility and have met or exceeded all health and safety guidelines.
3-5 year Kinder Funded Program
Story Time
Show and Tell
Puzzles and Games
Computer Time
Arts and Crafts
Music
Pre-Reading Activities
And much more
You can rest assured that your child will be cared for with the most kindness, love and respect. We believe all children are precious gifts and we treat them as though they are our own.
Full-time, part-time, Half days, Before, after-school schedules are available.
To learn more, contact us today! 03 9514 -0817 or info@brightpebbles.example.au

```html
<!DOCTYPE html>
<html lang="en">
<head>
<meta charset="utf-8">
<title>Bright Pebbles Child Care Centre</title>
<link rel="stylesheet" href="https://fonts.googleapis.com/css2?family=Cinzel+Decorative:wght@700&family=Courier+Prime&display=swap">
<style>
  :root {
    --ink: #2a14c4;
    --title: #3a16c0;
    --red: #ff3d57;
    --yellow: #ffd63f;
    --green: #62ee35;
    --frame-yellow: #ffd32a;
    --frame-blue: #2410c0;
    --frame-red: #f5475c;
    --paper: #ffffff;
  }
  html, body { margin: 0; padding: 0; overflow: hidden; background: var(--paper); }
  .ad {
    position: relative;
    width: 1200px;
    height: 998px;
    background: var(--paper);
    overflow: hidden;
    font-family: "Courier Prime", "Courier New", monospace;
    color: var(--ink);
  }
  .confetti-zone { position: absolute; inset: 0; }

  .photo {
    position: absolute;
    box-sizing: border-box;
    margin: 0;
    background: var(--paper);
  }
  .photo--party { left: 15px; top: 24px; width: 253px; height: 330px; border: 6px solid var(--frame-yellow); padding: 5px; }
  .photo--circle { left: 18px; top: 373px; width: 245px; height: 247px; border: 6px solid var(--frame-blue); padding: 6px; }
  .photo--slide { left: 15px; top: 637px; width: 253px; height: 330px; border: 6px solid var(--frame-red); padding: 6px; }
  .photo .inner { width: 100%; height: 100%; }
  .photo--party .inner { background: linear-gradient(180deg, #9a8c86 0%, #d07aa8 45%, #6f8f3e 100%); }
  .photo--circle .inner { background: linear-gradient(180deg, #3f9a3a 0%, #c2364a 50%, #2f6fa8 100%); }
  .photo--slide .inner { background: linear-gradient(180deg, #4d7a3e 0%, #c94a3a 45%, #e6b020 100%); }

  .title {
    position: absolute;
    left: 300px;
    top: 72px;
    width: 855px;
    margin: 0;
    text-align: center;
    font-family: "Cinzel Decorative", "Times New Roman", serif;
    font-weight: 700;
    font-size: 40px;
    line-height: 52px;
    color: var(--title);
    letter-spacing: 0.5px;
    white-space: nowrap;
  }
  .copy {
    position: absolute;
    margin: 0;
    font-size: 20px;
    line-height: 30px;
    white-space: pre;
  }
  .copy--intro { left: 601px; top: 166px; }
  .copy--licence { left: 598px; top: 411px; }
  .copy--promise { left: 595px; top: 596px; }
  .copy--offer { left: 278px; top: 672px; }
  .contact {
    position: absolute;
    left: 398px;
    top: 970px;
    margin: 0;
    font-size: 16px;
    line-height: 22px;
    white-space: nowrap;
  }
</style>
</head>
<body>
<main class="ad">
  <svg class="confetti-zone" width="1200" height="998" viewBox="0 0 1200 998" role="img" aria-label="Scattered confetti dots in red, yellow and green framing the text">
    <defs>
      <linearGradient id="confetti-tones" x1="0" y1="0" x2="1" y2="1">
        <stop offset="0" stop-color="#ff3d57"/>
        <stop offset="0.5" stop-color="#ffd63f"/>
        <stop offset="1" stop-color="#62ee35"/>
      </linearGradient>
      <filter id="soft-edge" x="-20%" y="-20%" width="140%" height="140%">
        <feGaussianBlur stdDeviation="18"/>
      </filter>
    </defs>
    <g fill="url(#confetti-tones)" opacity="0.28" filter="url(#soft-edge)">
      <rect x="282" y="20" width="300" height="720" rx="80"/>
      <rect x="470" y="750" width="700" height="200" rx="90"/>
      <rect x="1030" y="0" width="170" height="800" rx="70"/>
    </g>
  </svg>

  <figure class="photo photo--party">
    <div class="inner" role="img" aria-label="Photo of children in fairy costumes gathered on the grass with a carer"></div>
  </figure>
  <figure class="photo photo--circle">
    <div class="inner" role="img" aria-label="Photo of children in festive hats sitting in a circle on a blue mat with a carer"></div>
  </figure>
  <figure class="photo photo--slide">
    <div class="inner" role="img" aria-label="Photo of a young girl holding a baby on a yellow playground slide"></div>
  </figure>

  <h1 class="title">BRIGHT PEBBLES CHILD CARE CENTRE</h1>

  <p class="copy copy--intro">Bright Pebbles Child Care Centre
offers a safe, nurturing environment
where your child will get the attention
and care that he or she needs.
Our ratio of children to adults is
always within state guidelines - and
often even higher - to make certain
each child receives top-quality care.</p>

  <p class="copy copy--licence">We are also state licensed as a Child
Care facility and have met or exceeded
all health and safety guidelines.
We offer 3-5 year Kinder Funded Program.
Full-time, part-time, Half days, Before,
after-school schedules are also available.</p>

  <p class="copy copy--promise">You can rest assured that your child
will be cared for with the most kindness,
love and respect. We believe all children
are precious gifts and we treat them as
though they are our own.</p>

  <p class="copy copy--offer">We offer:
*Story Time
*Show and Tell
*Puzzles and Games
*Computer Time
*Arts and Crafts
*Music
*Pre-Reading Activities
And much more!</p>

  <p class="contact">To learn more, contact us today! 03 9514 -0817 or info@brightpebbles.example.au</p>
</main>
</body>
</html>
```